harbor mental health stationary

Please help turn this logo into a total image for my business.
Stationary need to be able to be individualized for each mental health practitioners

Some generic info about services
Clinical Psychology - Consultant Psychiatry - Locum Services - Medico-legal - Architectural Adviser Clinical and Medical Facilities

Target Market(s)

Letter head for doctors, courts, patients.

Industry/Entity Type

Mental Health

Requirements
Must have
• area where practitioners details can be listed and logo on page
Nice to have
• embossed section

```html
<!DOCTYPE html>
<html lang="en">
<head>
<meta charset="utf-8">
<title>Harbor Mental Health — Stationery</title>
<link href="https://fonts.googleapis.com/css2?family=Didact+Gothic&display=swap" rel="stylesheet">
<style>
  :root{
    --backdrop:#3d3e40;
    --paper:#ffffff;
    --navy:#163259;
    --navy-deep:#12294a;
    --navy-mid:#1a4f7a;
    --teal:#1a8db4;
    --teal-light:#2aa3c9;
    --ink:#4a4a4c;
    --ink-soft:#6d6e70;
    --rule:#d6d6d8;
    --band-grey:#6d6e70;
    --head-fill:#e6e6e8;
    --ghost:#f1f1f2;
  }
  *{margin:0;padding:0;box-sizing:border-box}
  html,body{width:1200px;height:1000px;overflow:hidden}
  body{background:var(--backdrop);font-family:"Didact Gothic",sans-serif;color:var(--ink);position:relative}

  .sheet{position:absolute;background:var(--paper);overflow:hidden}
  .sheet--cover{left:52px;top:123px;width:531px;height:758px}
  .sheet--letter{left:620px;top:120px;width:538px;height:762px}

  .cover-art{
    position:absolute;inset:0;
    background:linear-gradient(215deg,
      var(--paper) 0%, var(--paper) 25%,
      var(--teal-light) 31%, var(--navy) 45%,
      var(--navy-mid) 62%, var(--navy) 78%,
      #1d6f96 84%, var(--paper) 88%, var(--paper) 100%);
  }

  .brand{position:absolute;display:flex;align-items:center;gap:10px}
  .brand__square{background:var(--navy);flex:none}
  .brand__name{color:var(--navy);font-weight:400;line-height:1}
  .brand__name span{display:block}
  .sheet--cover .brand{left:297px;top:40px}
  .sheet--cover .brand__square{width:48px;height:48px}
  .sheet--cover .brand__main{font-size:28px;letter-spacing:1px}
  .sheet--cover .brand__sub{font-size:13px;letter-spacing:.6px;margin-top:3px}
  .sheet--letter .brand{left:38px;top:30px;gap:8px}
  .sheet--letter .brand__square{width:33px;height:33px}
  .sheet--letter .brand__main{font-size:19px;letter-spacing:.6px}
  .sheet--letter .brand__sub{font-size:9px;letter-spacing:.4px;margin-top:2px}

  .office{position:absolute;font-style:normal;font-size:7px;line-height:9.5px;color:var(--ink-soft)}
  .office b{color:var(--navy);font-weight:400}
  .sheet--cover .office{left:37px;top:693px}
  .sheet--letter .office{left:398px;top:28px;font-size:6.4px;line-height:8.5px}

  .cover-web{position:absolute;left:396px;top:719px;font-size:9px;color:#fff}

  .letter-ghost{
    position:absolute;right:0;bottom:0;width:220px;height:280px;
    background:radial-gradient(ellipse at 100% 100%, var(--ghost) 0%, var(--ghost) 45%, rgba(241,241,242,0) 75%);
  }

  .letter-body{position:absolute;left:38px;top:124px;width:461px;font-size:9.9px;line-height:16px}
  .letter-body h1{font-size:9.9px;font-weight:400;color:#333;-webkit-text-stroke:.3px #333;margin-bottom:14px}
  .letter-body p{margin-bottom:14px}
  .letter-body ul{list-style:none;margin-bottom:20px;line-height:15.2px}

  .assessment{width:461px;border-collapse:collapse;font-size:9.6px;margin-bottom:14px}
  .assessment thead th{background:var(--head-fill);font-weight:400;text-align:left;height:21px;padding:0 12px;border-right:1px solid #fff}
  .assessment thead th.mark{text-align:center;padding:0}
  .assessment .spacer td{height:11px;border:none}
  .assessment tbody.rows td{border:1px solid var(--rule);height:37.6px;font-size:7.2px;line-height:9.5px;padding:0 10px}
  .assessment col.item{width:132px}
  .assessment col.mark{width:29px}
  .assessment col.note{width:184px}

  .letter-body p.closing{line-height:20px;text-align:justify;font-size:10.2px}

  .letter-band{position:absolute;left:0;top:740px;width:538px;height:17px}
  .letter-web{position:absolute;right:40px;top:743px;font-size:6.5px;color:#fff}
</style>
</head>
<body>

<section class="sheet sheet--cover">
  <div class="cover-art" role="img" aria-label="Decorative flowing blue and teal cover artwork"></div>

  <div class="brand">
    <div class="brand__square"></div>
    <div class="brand__name"><span class="brand__main">HARBOR</span><span class="brand__sub">MENTAL HEALTH</span></div>
  </div>

  <address class="office">
    <b>Head Office:</b> Suite 410,<br>No.27/B Quay Road, Portside<br>Tel: +1 (555) 014 2200<br>Fax: +1 (555) 014 2201
  </address>
  <div class="cover-web">www.harbormh.com</div>
</section>

<section class="sheet sheet--letter">
  <div class="letter-ghost" role="img" aria-label="Faint decorative corner artwork"></div>

  <div class="brand">
    <div class="brand__square"></div>
    <div class="brand__name"><span class="brand__main">HARBOR</span><span class="brand__sub">MENTAL HEALTH</span></div>
  </div>

  <address class="office">
    <b>Head Office:</b> Suite 410,<br>No.27/B Quay Road, Portside<br>Tel: +1 (555) 014 2200<br>Fax: +1 (555) 014 2201
  </address>

  <article class="letter-body">
    <h1>Lorem ipsum dolor sit amet.</h1>
    <p>Consectetuer adipiscing elit. Aenean commodo ligula eget dolor. Aenean massa. Cum sociis natoque penatibus et magnis dis parturient montes. nascetur ridiculus mus.</p>
    <ul>
      <li>- Donec quam felis. ultricies nec. pellentesque eu.</li>
      <li>- Pretium quis. sem. Nulla consequat massa quis enim.</li>
      <li>- Donec pede justo. fringilla vel. aliquet nec.</li>
      <li>- Vulputate eget. arcu. Itis vitae. justo.</li>
    </ul>

    <table class="assessment">
      <colgroup><col class="item"><col class="mark"><col class="mark"><col class="mark"><col class="note"><col></colgroup>
      <thead>
        <tr><th>Lorem ipsum dolor sit</th><th class="mark">M</th><th class="mark">A</th><th class="mark">D</th><th>Note</th><th></th></tr>
      </thead>
      <tbody><tr class="spacer"><td colspan="6"></td></tr></tbody>
      <tbody class="rows">
        <tr><td>Donec quam felis. ultricies<br>nec. pellentesque eu</td><td></td><td></td><td></td><td></td><td></td></tr>
        <tr><td>Donec quam felis. ultricies<br>nec. pellentesque eu</td><td></td><td></td><td></td><td></td><td></td></tr>
        <tr><td>Donec quam felis. ultricies<br>nec. pellentesque eu</td><td></td><td></td><td></td><td></td><td></td></tr>
        <tr><td>Donec quam felis. ultricies<br>nec. pellentesque eu</td><td></td><td></td><td></td><td></td><td></td></tr>
        <tr><td>Donec quam felis. ultricies<br>nec. pellentesque eu</td><td></td><td></td><td></td><td></td><td></td></tr>
      </tbody>
    </table>

    <p class="closing">Nullam dictum felis eu pede mollis pretium. Integer tincidunt. Cras dapibus. Vivamus elementum semper nisi. Aenean vulputate eleifend tellus. Aenean leo ligula. porttitor eu. consequat vitae. eleifend ac. enim. Aliquam lorem ante. dapibus in. viverra quis. feugiat a. tellus. Phasellus viverra nulla ut metus varius laoreet. Quisque rutrum. Aenean imperdiet. Etiam ultricies nisi vel augue. Curabitur ullamcorper ultricies nisi.</p>
  </article>

  <svg class="letter-band" viewBox="0 0 538 17" preserveAspectRatio="none" aria-hidden="true">
    <defs>
      <linearGradient id="bandBlue" x1="0" y1="0" x2="1" y2="0">
        <stop offset="0" stop-color="#1a9cc6"/>
        <stop offset="1" stop-color="#163259"/>
      </linearGradient>
    </defs>
    <rect x="0" y="0" width="415" height="17" fill="url(#bandBlue)"/>
    <path d="M398,0 L538,0 L538,17 L418,17 Z" fill="#ffffff"/>
    <path d="M408,0 L538,0 L538,17 L428,17 Z" fill="var(--band-grey)"/>
  </svg>
  <div class="letter-web">www.harbormh.com</div>
</section>

</body>
</html>
```